Concise,Good colour matching,Good looks design for "HERD SURE RAPID TEST FOR LIVESTOCK"

Product Positioning: Affordable test for Large Animals (Livestock/Veterinary Use)
Product Name: HERD SURE Rapid Test Kit (for large animals, e.g., cattle, horses, swine,Avian,sheep).

2. Packaging Requirements

A. Visual Design
Color Scheme:
Green/Blue/Orange/Yellow/Red/Gray/White(chose 2~4 colors)

Mandatory Info:
Brand logo ("HERD SURE")

Target Market(s)

Southeast Asia, Africa, Middle East, South America

Industry/Entity Type

Veterinary diagnostic for LIVESTOCK

Colors

Designer to choose colors to be used in the design.

Requirements
Nice to have
• Concise,Good colour matching,Good looks

```html
<!DOCTYPE html>
<html lang="en">
<head>
<meta charset="utf-8">
<title>HERD SURE Rapid Test Kit – Carton Dieline</title>
<link rel="stylesheet" href="https://fonts.googleapis.com/css2?family=Montserrat:wght@400;500;700;800&family=Poppins:wght@400;600&display=swap">
<style>
  :root {
    --navy: #1b3a6b;
    --orange: #ef8a1f;
    --green: #7ab648;
    --grey: #a7a9ac;
    --white: #ffffff;
    --cut: #d6245f;
    --fold: #6ec6e8;
    --page: #ffffff;
  }
  html, body {
    margin: 0;
    width: 727px;
    height: 1200px;
    overflow: hidden;
    background: var(--page);
  }
  .dieline {
    position: absolute;
    top: 187px;
    left: 0;
    width: 727px;
    height: 825px;
  }
  .cut { fill: none; stroke: var(--cut); stroke-width: 2; }
  .fold { fill: none; stroke: var(--fold); stroke-width: 1; }
  .fill-navy { fill: var(--navy); }
  .fill-grey { fill: var(--grey); }
  .fill-white { fill: var(--white); }
  .fill-green { fill: var(--green); }
  .brand { font-family: "Montserrat", sans-serif; font-weight: 800; }
  .tagline { font-family: "Montserrat", sans-serif; font-weight: 700; font-size: 15px; }
  .caption { font-family: "Montserrat", sans-serif; font-weight: 500; }
  .maker { font-family: "Montserrat", sans-serif; font-size: 8px; }
  .maker-name { font-weight: 800; font-size: 11px; }
  .bullet { font-family: "Montserrat", sans-serif; font-size: 12px; fill: var(--white); }
  .badge-text { font-family: "Montserrat", sans-serif; font-weight: 800; font-size: 10px; fill: var(--white); }
  .side-copy { font-family: "Poppins", sans-serif; font-size: 11px; fill: var(--navy); }
  .side-head { font-family: "Poppins", sans-serif; font-weight: 600; font-size: 11px; fill: var(--navy); }
  .side-note { font-family: "Poppins", sans-serif; font-size: 10.5px; fill: var(--white); }
</style>
</head>
<body>
<svg class="dieline" viewBox="226 40 1042 1180" xmlns="http://www.w3.org/2000/svg">
  <defs>
    <g id="front-face">
      <rect class="fill-grey" x="525" y="413" width="443" height="15"/>
      <rect class="fill-navy" x="525" y="428" width="443" height="222"/>
      <text class="brand" x="746" y="490" text-anchor="middle" font-size="50" fill="var(--white)">HERD SURE</text>
      <text class="tagline" x="755" y="526" text-anchor="middle" fill="var(--white)">AFFORDABLE DIAGNOSTICS FOR HEALTHY HERDS</text>
      <circle cx="574" cy="553" r="3.5" class="fill-white"/>
      <circle cx="574" cy="572" r="3.5" class="fill-white"/>
      <circle cx="574" cy="591" r="3.5" class="fill-white"/>
      <text class="bullet" x="586" y="557">FAST &amp; EFFICENT</text>
      <text class="bullet" x="586" y="576">AFFORDABLE</text>
      <text class="bullet" x="586" y="595">RELIABLE &amp; SIMPLE</text>
      <g class="time-badge">
        <circle cx="898" cy="577" r="17" fill="var(--orange)"/>
        <circle cx="898" cy="577" r="13" fill="none" stroke="var(--white)" stroke-width="1.2" stroke-dasharray="3 2"/>
        <text x="898" y="576" text-anchor="middle" class="badge-text" font-size="8">10</text>
        <text x="898" y="585" text-anchor="middle" class="badge-text" font-size="7">MIN</text>
      </g>
      <text class="badge-text" x="898" y="610" text-anchor="middle">RAPID RESULTS</text>
      <text class="badge-text" x="898" y="625" text-anchor="middle">IN 10 MINUTES</text>
      <text class="maker" x="540" y="628" fill="var(--white)">Manufactured by <tspan class="maker-name">FIELDLINE</tspan></text>
    </g>
  </defs>

  <!-- top tuck flap -->
  <path class="fill-navy" d="M525 93 V80 Q525 45 565 45 H928 Q968 45 968 80 V93 Z"/>
  <path class="cut" d="M525 93 V80 Q525 45 565 45 H928 Q968 45 968 80 V93"/>

  <!-- lid panel -->
  <rect class="fill-white" x="525" y="93" width="443" height="217"/>
  <rect class="fill-grey" x="525" y="310" width="443" height="13"/>
  <rect class="fill-navy" x="525" y="323" width="443" height="90"/>
  <text class="brand" x="746" y="172" text-anchor="middle" font-size="50" fill="var(--orange)">HERD SURE</text>
  <text class="tagline" x="747" y="204" text-anchor="middle" fill="var(--navy)">AFFORDABLE DIAGNOSTICS FOR HEALTHY HERDS</text>
  <g class="species-icons">
    <circle cx="620" cy="255" r="24" class="fill-green" stroke="var(--white)" stroke-width="2" role="img" aria-label="Horse icon"/>
    <circle cx="683" cy="255" r="24" class="fill-green" stroke="var(--white)" stroke-width="2" role="img" aria-label="Cattle icon"/>
    <circle cx="746" cy="255" r="24" class="fill-green" stroke="var(--white)" stroke-width="2" role="img" aria-label="Swine icon"/>
    <circle cx="809" cy="255" r="24" class="fill-green" stroke="var(--white)" stroke-width="2" role="img" aria-label="Sheep icon"/>
    <circle cx="872" cy="255" r="24" class="fill-green" stroke="var(--white)" stroke-width="2" role="img" aria-label="Poultry icon"/>
  </g>
  <text class="caption" x="746" y="370" text-anchor="middle" font-size="19" fill="var(--white)">LARGE ANIMAL RAPID TEST CARD</text>
  <text class="maker" x="531" y="403" fill="var(--white)">Manufactured by <tspan class="maker-name">FIELDLINE</tspan></text>
  <path class="cut" d="M525 93 V413 M968 93 V413"/>

  <!-- front panel -->
  <use href="#front-face"/>

  <!-- front dust flaps -->
  <path class="cut" d="M525 413 L437 420 V643 L525 650"/>
  <path class="cut" d="M968 413 L1057 420 V643 L968 650"/>

  <!-- base panel -->
  <rect class="fill-white fold" x="525" y="650" width="443" height="325"/>

  <!-- left side panel -->
  <rect class="fill-white fold" x="289" y="650" width="236" height="325"/>
  <path class="cut" d="M289 650 L282 660 L229 663 V958 L275 973 L289 975"/>
  <g transform="rotate(-90 0 0)">
    <text class="brand" x="-812" y="323" text-anchor="middle" font-size="30" fill="var(--orange)">HERD SURE</text>
    <text class="side-copy" x="-884" y="346">Manufactured by FIELDLINE</text>
    <text class="side-copy" x="-890" y="376">Storage: 2-30°C,Do not freeze</text>
    <text class="side-copy" x="-872" y="401">For veterinary use only.</text>
    <text class="side-copy" x="-890" y="426">Keep out of reach of children.</text>
    <text class="side-copy" x="-900" y="451">Dispose of test properly after use.</text>
    <text class="side-copy" x="-912" y="476">See the instructions for other contents</text>
  </g>
  <g class="handling-marks" fill="var(--navy)">
    <rect x="492" y="855" width="14" height="14" rx="2"/>
    <rect x="492" y="831" width="14" height="14" rx="2"/>
    <rect x="492" y="807" width="14" height="14" rx="2"/>
    <rect x="492" y="783" width="14" height="14" rx="2"/>
    <rect x="492" y="755" width="14" height="20" rx="2"/>
  </g>

  <!-- right side panel -->
  <rect class="fill-white fold" x="968" y="650" width="237" height="325"/>
  <path class="cut" d="M1205 650 L1212 660 L1264 663 V958 L1218 973 L1205 975"/>
  <rect class="fill-grey" x="1100" y="670" width="28" height="286"/>
  <rect class="fill-grey" x="1040" y="670" width="28" height="286"/>
  <rect class="fill-grey" x="981" y="670" width="28" height="286"/>
  <g transform="rotate(90 0 0)">
    <text class="brand" x="812" y="-1168" text-anchor="middle" font-size="30" fill="var(--orange)">HERD SURE</text>
    <text class="side-head" x="772" y="-1136">Fast &amp; Efficient:</text>
    <text class="side-note" x="673" y="-1115">Rapid test results in less than 10 minutes from prep to</text>
    <text class="side-note" x="673" y="-1103">completion.</text>
    <text class="side-head" x="784" y="-1076">Affordable:</text>
    <text class="side-note" x="673" y="-1055">Colloidal gold-based rapid tests that combine high ac-</text>
    <text class="side-note" x="673" y="-1043">curacy with cost-effectiveness.</text>
    <text class="side-head" x="766" y="-1016">Reliable &amp; Simple:</text>
    <text class="side-note" x="673" y="-995">Stable test performance with 2-30°C,Easy to oper-</text>
    <text class="side-note" x="673" y="-983">ate,no professional skills required.</text>
  </g>

  <!-- back panel (inverted) -->
  <use href="#front-face" transform="rotate(180 746.5 812.5)"/>
  <rect class="fill-grey" x="525" y="1197" width="443" height="14"/>
  <path class="fill-white" d="M730 1211 Q732 1191 746 1191 Q760 1191 763 1211 Z"/>
  <path class="cut" d="M525 1213 H730 Q732 1191 746 1191 Q760 1191 763 1213 H968"/>

  <!-- back dust flaps -->
  <path class="cut" d="M525 975 L437 983 V1205 L525 1213"/>
  <path class="cut" d="M968 975 L1057 983 V1205 L968 1213"/>
</svg>
</body>
</html>
```